Update our insurance company Business Card

Create a more current card with two locations. Atlanta & Lake Oconee. Please make suggestions for: photo or no photos, back of card, type of material etc. We are risk advisors / insurance brokers and cater to businesses and the affluent home owner. We have been in a luxury resort community for 8 years and are expanding to a second location in Atlanta.

Target Market(s)

We are risk advisors / insurance brokers and cater to businesses (Tech, Healthcare, Restaurants, Hotels, Commercial property) and the affluent home owner. We have been in a luxury resort community for 8 years and are expanding to a second location in Atlanta.

Industry/Entity Type

Insurance

Contact Information for Business Card

Tavish K. Merriam, CLCS
President & CEO

Lake Oconee: 555-014-2267
Atlanta: TBD
Fax: 555-014-2268
E-Mail: Tavish@mwcoverageteam.com

Website: www.mwcoverageteam.com

Colors

Designer to choose colors to be used in the design.

Requirements
Must have
• LOGO. I will need phone #'s for Atlanta, Lake Oconee, Mobile, and Fax. Website and e-mail. Must have cropped photo chest up or face.
Nice to have
• Please make suggestions for: QR Code or something better, photo, back of card, type of material etc. Red edging. See file.

```html
<!DOCTYPE html>
<html lang="en">
<head>
<meta charset="utf-8">
<title>M&amp;W Coverage Team — Business Card</title>
<link rel="stylesheet" href="https://fonts.googleapis.com/css2?family=Tinos:wght@400;700&display=swap">
<style>
  :root {
    --stage: #e9e6e1;
    --card-white: #ffffff;
    --card-grey: #e6e7e9;
    --halo: #f1f2f3;
    --brand-red: #e3202a;
    --ink: #1a1a1a;
    --paper-text: #ffffff;
    --photo-tone: #7a6a5c;
    --photo-tone-dark: #2a3550;
  }
  * { box-sizing: border-box; margin: 0; padding: 0; }
  html, body {
    width: 1200px; height: 800px; overflow: hidden;
    background: var(--stage);
    font-family: "Tinos", "Times New Roman", serif;
  }
  .canvas {
    position: relative; width: 1200px; height: 800px;
    display: flex; align-items: center; justify-content: center; gap: 40px;
  }
  .card {
    position: relative; width: 540px; height: 309px;
    border-radius: 4px; overflow: hidden;
    box-shadow: 0 8px 24px rgba(0,0,0,.18);
  }

  /* Front: logo side */
  .card--front {
    background: radial-gradient(circle at 50% 40%, var(--card-white) 0%, #eeeeee 100%);
    display: flex; flex-direction: column; align-items: center; justify-content: center; gap: 10px;
  }
  .brand { display: flex; align-items: center; gap: 12px; }
  .brand__mark { width: 22px; height: 22px; background: var(--brand-red); }
  .brand__name {
    font-weight: 700; font-size: 34px; color: var(--ink);
    letter-spacing: .5px; text-transform: uppercase;
  }
  .brand__tagline {
    font-weight: 700; font-size: 15px; color: var(--brand-red);
    letter-spacing: .4px; font-variant: small-caps;
  }

  /* Back: contact side */
  .card--back { background: var(--card-grey); }
  .card__band {
    position: absolute; left: 0; right: 0; bottom: 0; height: 100px;
    background: var(--brand-red);
  }
  .contact__name {
    position: absolute; left: 30px; top: 26px;
    font-weight: 700; font-size: 24px; color: var(--brand-red);
  }
  .contact__title { position: absolute; left: 30px; top: 56px; font-size: 17px; color: var(--ink); }
  .contact__phones {
    position: absolute; left: 30px; top: 104px;
    list-style: none; font-size: 17px; line-height: 24px; color: var(--ink);
  }
  .contact__links {
    position: absolute; left: 30px; top: 226px;
    list-style: none; font-size: 17px; line-height: 28px; color: var(--paper-text);
  }
  .contact__links li { display: flex; align-items: center; gap: 8px; }
  .contact__links svg { width: 16px; height: 16px; flex: none; }
  .portrait-halo {
    position: absolute; left: 340px; top: 70px; width: 200px; height: 200px;
    border-radius: 50%; background: var(--halo);
  }
  .portrait {
    position: absolute; left: 362px; top: 92px; width: 156px; height: 156px;
    border-radius: 50%; border: 4px solid var(--card-white);
    background: linear-gradient(180deg, var(--photo-tone) 0%, var(--photo-tone) 55%, var(--photo-tone-dark) 100%);
  }
</style>
</head>
<body>
<main class="canvas">
  <section class="card card--front" aria-label="Card front">
    <div class="brand">
      <span class="brand__mark" aria-hidden="true"></span>
      <span class="brand__name">M&amp;W Coverage Team, LLC</span>
    </div>
    <p class="brand__tagline">Stay Calm When You're Covered With M&amp;W</p>
  </section>

  <section class="card card--back" aria-label="Card back">
    <div class="card__band"></div>
    <h1 class="contact__name">Tavish K. Merriam, CLCS</h1>
    <p class="contact__title">President &amp; CEO</p>
    <ul class="contact__phones">
      <li>Lake Oconee: 555-014-2267</li>
      <li>Atlanta: TBD</li>
      <li>Fax: 555-014-2268</li>
    </ul>
    <ul class="contact__links">
      <li>
        <svg viewBox="0 0 16 16" aria-hidden="true"><rect x="1.5" y="3.5" width="13" height="9" fill="none" stroke="#fff" stroke-width="1.3"/><path d="M1.5 3.5 8 9l6.5-5.5" fill="none" stroke="#fff" stroke-width="1.3"/></svg>
        Tavish@mwcoverageteam.com
      </li>
      <li>
        <svg viewBox="0 0 16 16" aria-hidden="true"><circle cx="8" cy="8" r="6.5" fill="none" stroke="#fff" stroke-width="1.3"/><ellipse cx="8" cy="8" rx="2.8" ry="6.5" fill="none" stroke="#fff" stroke-width="1.1"/><path d="M1.5 8h13" stroke="#fff" stroke-width="1.1"/></svg>
        www.mwcoverageteam.com
      </li>
    </ul>
    <div class="portrait-halo" aria-hidden="true"></div>
    <div class="portrait" role="img" aria-label="Cropped chest-up portrait photo of the company president"></div>
  </section>
</main>
</body>
</html>
```